Business Card for Holistic Health Business
Bright Ferns Natural Wellness & Live Cell Review
Use same font as used in my logo
Not sure, I am open to different fonts.
Simple
Marla Dunwoody
DynBC, CH, BA
Larkvale Acupuncture Clinic
2736-18 Avenue, Suite 200
Larkvale, AB T8K 2P6
brightferns@mailnest.ca
www.brightfernsnaturalwellness.com
Logo for Bright Ferns business card.

```html
<!DOCTYPE html>
<html lang="en">
<head>
<meta charset="utf-8">
<title>Bright Ferns Business Card</title>
<link rel="stylesheet" href="https://fonts.googleapis.com/css2?family=Open+Sans:wght@300;400;700&display=swap">
<style>
  :root {
    --backdrop: #e9e6e1;
    --card-white: #ffffff;
    --card-black: #0b0b0b;
    --accent-blue: #3d8ed6;
    --ink: #1a1a1a;
    --rule-grey: #6b6b6b;
    --text-light: #f2f2f2;
  }
  * { margin: 0; padding: 0; box-sizing: border-box; }
  html, body {
    width: 1200px; height: 902px; overflow: hidden;
    background: var(--backdrop);
    font-family: "Open Sans", Arial, sans-serif;
  }
  .card {
    position: absolute; left: 120px; top: 177px;
    width: 960px; height: 548px;
    background: var(--card-white);
    overflow: hidden;
    box-shadow: 0 10px 30px rgba(0,0,0,0.18);
  }
  .card-bands { position: absolute; inset: 0; }
  .brand {
    position: absolute; left: 300px; top: 62px; width: 460px;
  }
  .brand-mark {
    position: absolute; left: -4px; top: 0;
    width: 30px; height: 30px; border-radius: 50%;
    background: var(--accent-blue);
  }
  .brand-name {
    margin-left: 40px;
    font-weight: 300; font-size: 64px; line-height: 1.1;
    color: var(--ink); letter-spacing: 1px;
  }
  .brand-tagline {
    margin-left: 40px; margin-top: 6px;
    padding-top: 4px;
    border-top: 2px solid var(--rule-grey);
    font-size: 17px; color: var(--ink); letter-spacing: 0.3px;
  }
  .person {
    position: absolute; left: 48px; top: 318px;
    color: var(--text-light);
  }
  .person-name { font-weight: 700; font-size: 25px; }
  .person-credentials { font-size: 18px; margin-top: 8px; }
  .contact {
    position: absolute; left: 560px; top: 282px;
    list-style: none; color: var(--text-light);
    font-size: 17px; line-height: 1.35;
  }
  .contact-item { display: flex; align-items: flex-start; gap: 12px; margin-bottom: 4px; }
  .contact-icon { flex: 0 0 18px; width: 18px; height: 18px; margin-top: 2px; }
  .contact-lines { display: block; }
</style>
</head>
<body>
  <div class="card">
    <svg class="card-bands" width="960" height="548" viewBox="0 0 960 548" aria-hidden="true">
      <rect x="0" y="252" width="960" height="296" fill="var(--card-black)"/>
      <polygon points="0,240 330,240 330,252 0,252" fill="var(--card-black)"/>
      <polygon points="22,252 60,252 22,282" fill="var(--accent-blue)"/>
      <polygon points="0,440 330,440 380,470 960,470 960,488 0,488" fill="var(--accent-blue)"/>
    </svg>

    <div class="brand">
      <span class="brand-mark"></span>
      <div class="brand-name">Bright Ferns</div>
      <div class="brand-tagline">Bright Ferns Natural Wellness &amp; Live Cell Review</div>
    </div>

    <div class="person">
      <div class="person-name">Marla Dunwoody</div>
      <div class="person-credentials">DynBC, CH, BA</div>
    </div>

    <ul class="contact">
      <li class="contact-item">
        <svg class="contact-icon" viewBox="0 0 18 18" aria-hidden="true">
          <circle cx="9" cy="9" r="9" fill="var(--text-light)"/>
          <path d="M9 3.5a3.3 3.3 0 0 0-3.3 3.3C5.7 9.3 9 14 9 14s3.3-4.7 3.3-7.2A3.3 3.3 0 0 0 9 3.5z" fill="var(--card-black)"/>
          <circle cx="9" cy="6.8" r="1.2" fill="var(--text-light)"/>
        </svg>
        <span class="contact-lines">Larkvale Acupuncture Clinic<br>2736-18 Avenue, Suite 200<br>Larkvale, AB T8K 2P6</span>
      </li>
      <li class="contact-item">
        <svg class="contact-icon" viewBox="0 0 18 18" aria-hidden="true">
          <circle cx="9" cy="9" r="9" fill="var(--text-light)"/>
          <path d="M6 4.5l1.8 2.2-1 1.2c.7 1.4 1.7 2.4 3.1 3.1l1.2-1 2.2 1.8-1 1.6C9 13.2 4.8 9 4.4 5.5z" fill="var(--card-black)"/>
        </svg>
        <span>780.555.0142</span>
      </li>
      <li class="contact-item">
        <svg class="contact-icon" viewBox="0 0 18 18" aria-hidden="true">
          <circle cx="9" cy="9" r="9" fill="var(--text-light)"/>
          <rect x="4.5" y="6" width="9" height="6.5" fill="var(--card-black)"/>
          <path d="M4.5 6l4.5 3.6L13.5 6" fill="none" stroke="var(--text-light)" stroke-width="0.9"/>
        </svg>
        <span>brightferns@mailnest.ca</span>
      </li>
      <li class="contact-item">
        <svg class="contact-icon" viewBox="0 0 18 18" aria-hidden="true">
          <circle cx="9" cy="9" r="9" fill="var(--text-light)"/>
          <circle cx="9" cy="9" r="4.5" fill="none" stroke="var(--card-black)" stroke-width="1.1"/>
          <ellipse cx="9" cy="9" rx="2" ry="4.5" fill="none" stroke="var(--card-black)" stroke-width="1"/>
          <line x1="4.5" y1="9" x2="13.5" y2="9" stroke="var(--card-black)" stroke-width="1"/>
        </svg>
        <span>www.brightfernsnaturalwellness.com</span>
      </li>
    </ul>
  </div>
</body>
</html>
```